Lumen Cove Skincare - Package Design

New Beauty label needing product packaging design. Looking for elegant and stylish design to represent our premium brand.

This project is for 1 label and 1 box design. The winning designer will be assigned another project for the next product in the range. (to be paid as a new project)

This product is for "Dead Sea Mud Mask". Please see the label format and jar attached. Please note there are 2 different jars we are considering (will have a mud inside). Please feel free to choose whichever one suits your design best.

The labels and boxes are to retain the product information, such as size, ingredients etc, but is to be updated to our brand. You can move or display the other information as you wish.

the size of the dead sea mud mask color box is 72*72*85mm (length*width*height)
the size of dead sea mud mask label is 218*58mm (width*height)

Target Market(s)

Women 15 to 65

Requirements
Must have
• Must be elegant and represent our brand which is a premium beauty product.
Should not have
• Dark blue. Dark purple etc. Colours should compliment the logo

```html
<!DOCTYPE html>
<html lang="en">
<head>
<meta charset="utf-8">
<title>Lumen Cove Skincare – Dead Sea Mud Mask Packaging</title>
<link href="https://fonts.googleapis.com/css2?family=Josefin+Sans:wght@300;400&family=Arimo:wght@400&family=Delius&display=swap" rel="stylesheet">
<style>
  :root {
    --backdrop: #e4e4e4;
    --panel-dark: #141414;
    --panel-mid: #262626;
    --gold: #c9a24a;
    --gold-light: #e6c878;
    --ink-light: #f1f1f1;
    --ink-soft: #d8d8d8;
  }
  * { margin: 0; padding: 0; box-sizing: border-box; }
  html, body { width: 1200px; height: 829px; overflow: hidden; background: var(--backdrop); }
  .stage { position: relative; width: 1200px; height: 829px; }

  .pack-panel {
    position: absolute;
    background:
      radial-gradient(ellipse at 40% 30%, var(--panel-mid) 0%, var(--panel-dark) 70%);
    color: var(--ink-light);
    text-align: center;
    overflow: hidden;
  }
  .jar-label { left: 130px; top: 312px; width: 340px; height: 350px; }
  .box-front { left: 612px; top: 192px; width: 392px; height: 476px; }

  .brand {
    position: absolute; left: 0; right: 0;
    display: flex; align-items: center; justify-content: center; gap: 10px;
    font-family: "Josefin Sans", sans-serif; font-weight: 400;
    color: var(--gold); letter-spacing: 0.04em;
  }
  .brand-dot { border: 1.5px solid var(--gold); border-radius: 50%; flex: none; }
  .jar-label .brand { top: 56px; font-size: 21px; }
  .jar-label .brand-dot { width: 14px; height: 14px; }
  .box-front .brand { top: 118px; font-size: 26px; }
  .box-front .brand-dot { width: 17px; height: 17px; }

  .product-name {
    position: absolute; left: 0; right: 0;
    font-family: "Josefin Sans", sans-serif; font-weight: 300;
    line-height: 1;
  }
  .product-name .line-top { display: block; letter-spacing: 0.18em; }
  .product-name .line-bottom { display: block; }
  .product-name .mask-word { font-weight: 400; }
  .jar-label .product-name { top: 148px; }
  .jar-label .line-top { font-size: 30px; }
  .jar-label .line-bottom { font-size: 30px; margin-top: 6px; }
  .jar-label .mask-word { font-size: 44px; }
  .box-front .product-name { top: 196px; }
  .box-front .line-top { font-size: 36px; }
  .box-front .line-bottom { font-size: 36px; margin-top: 6px; }
  .box-front .mask-word { font-size: 54px; }

  .claims {
    position: absolute; left: 0; right: 0;
    font-family: "Arimo", sans-serif; color: var(--ink-soft);
    letter-spacing: 0.04em; word-spacing: 0.15em;
  }
  .jar-label .claims { top: 242px; font-size: 15.5px; }
  .box-front .claims { top: 310px; font-size: 17px; }

  .tagline {
    position: absolute; left: 0; right: 0;
    font-family: "Delius", cursive; color: var(--ink-soft); letter-spacing: 0.08em;
  }
  .jar-label .tagline { top: 266px; font-size: 15px; }
  .box-front .tagline { top: 336px; font-size: 16.5px; }

  .net-weight {
    position: absolute; left: 0; right: 0;
    font-family: "Arimo", sans-serif; color: var(--ink-light); letter-spacing: 0.03em;
  }
  .jar-label .net-weight { top: 308px; font-size: 15.5px; }
  .box-front .net-weight { top: 430px; font-size: 16px; }

  .gold-band {
    position: absolute; left: 0; right: 0; height: 4px;
    background: linear-gradient(90deg, var(--gold) 0%, var(--gold-light) 50%, var(--gold) 100%);
  }
  .jar-label .gold-band { bottom: 10px; }
  .box-front .gold-band { bottom: 10px; height: 5px; }
</style>
</head>
<body>
<main class="stage">
  <section class="pack-panel jar-label" aria-label="Jar label">
    <div class="brand"><span class="brand-dot"></span>Lumen Cove Skincare</div>
    <h1 class="product-name">
      <span class="line-top">DEAD SEA</span>
      <span class="line-bottom">MUD <span class="mask-word">MASK</span></span>
    </h1>
    <p class="claims">100% NATURAL &nbsp;-&nbsp; MINERAL RICH</p>
    <p class="tagline">Detoxifies and Restores</p>
    <p class="net-weight">250 GRAMS / 8.8 OZ</p>
    <div class="gold-band"></div>
  </section>

  <section class="pack-panel box-front" aria-label="Box front panel">
    <div class="brand"><span class="brand-dot"></span>Lumen Cove Skincare</div>
    <h2 class="product-name">
      <span class="line-top">DEAD SEA</span>
      <span class="line-bottom">MUD <span class="mask-word">MASK</span></span>
    </h2>
    <p class="claims">100% NATURAL &nbsp;-&nbsp; MINERAL RICH</p>
    <p class="tagline">Detoxifies and Restores</p>
    <p class="net-weight">250 GRAMS / 8.8 OZ</p>
    <div class="gold-band"></div>
  </section>
</main>
</body>
</html>
```